LOCAL TAXI SERVICE NEEDS A BANNER AD DESIGN

NEED BANNER AD DESIGN FOR TAXI SERVICE IN NJ. WE PROVIDE LOCAL AND LONG DISTANCE TRANSPORTATION. OUR MAIN BASE OF CUSTOMER GO TO THE MAJOR AIRPORTS IN THE TRI STATE AREA. I WANT TO OFFER A SPECIAL GOING TO HOLMBRIDGE AIRPORT OF $35.00 WITH A COUPON CODE OF PW 12. THIS BANNER AD WILL BE USED FOR MY PALWIRE PAGE

Target Market(s)

PEOPLE WHO TRAVEL A LOT

Industry/Entity Type

Taxi

Font styles to use
Serif
Sans Serif

Colors
0792cd
0255a3
33a6d7
85cae6
cee9f5
ecf7fb
ffffff

Requirements
Must have
• MY COMPANY NAME: DORVAN'S TAXI

```html
<!DOCTYPE html>
<html lang="en">
<head>
<meta charset="utf-8">
<title>Dorvan's Taxi – Airport Banner</title>
<link rel="stylesheet" href="https://fonts.googleapis.com/css2?family=Oswald:wght@400;700&family=Russo+One&family=Noto+Serif:wght@700&family=Roboto:wght@400&display=swap">
<style>
  :root {
    --ocean: #0792cd;
    --navy: #0255a3;
    --sky: #33a6d7;
    --mist: #85cae6;
    --ice: #cee9f5;
    --paper: #ecf7fb;
    --white: #ffffff;
  }
  * { margin: 0; padding: 0; box-sizing: border-box; }
  html, body { width: 1200px; height: 960px; overflow: hidden; }
  body { background: var(--paper); position: relative; font-family: "Roboto", sans-serif; }

  .banner {
    position: absolute; left: 14px; top: 256px; width: 1156px; height: 388px;
    background: linear-gradient(100deg, var(--sky) 0%, #2a86cf 35%, #2d6cc0 70%, var(--navy) 100%);
    overflow: hidden;
  }
  .skyline {
    position: absolute; left: 100px; right: 0; bottom: 0; height: 300px;
    background: linear-gradient(180deg, rgba(206,233,245,0) 0%, rgba(206,233,245,0.22) 55%, rgba(206,233,245,0.3) 100%);
  }
  .brand {
    position: absolute; left: 16px; top: 10px; height: 38px;
    display: flex; align-items: center; gap: 8px;
    background: #0c0c0c; padding: 0 12px 0 6px;
  }
  .brand-square { width: 26px; height: 26px; background: var(--white); }
  .brand-name {
    font-family: "Roboto", sans-serif; font-weight: 400; font-size: 30px;
    color: var(--white); letter-spacing: 0.5px; line-height: 1;
  }
  .headline {
    position: absolute; left: 440px; top: 5px; width: 690px; text-align: center;
    font-family: "Russo One", sans-serif; font-size: 37px; color: var(--ice);
    letter-spacing: 0.5px;
  }
  .promo {
    position: absolute; left: 17px; top: 109px; width: 360px; height: 98px;
    border: 1.5px solid var(--ice); text-align: center; color: var(--white);
    padding-top: 6px;
  }
  .promo-offer { font-family: "Oswald", sans-serif; font-weight: 700; font-size: 20px; }
  .promo-offer .amount { font-size: 40px; vertical-align: -4px; }
  .promo-code { font-family: "Roboto", sans-serif; font-size: 22px; letter-spacing: 1.5px; margin-top: 2px; }

  .route { position: absolute; top: 0; width: 210px; text-align: center; }
  .route-label {
    position: absolute; left: 0; right: 0; top: 66px;
    font-family: "Noto Serif", serif; font-weight: 700; font-size: 25px;
    line-height: 26px; color: var(--white); letter-spacing: 1.5px;
  }
  .route-tick { position: absolute; left: 103px; top: 124px; width: 4px; height: 12px; background: var(--white); }
  .route-photo {
    position: absolute; left: 8px; top: 136px; width: 194px; height: 194px;
    border-radius: 50%; border: 6px solid var(--white);
  }
  .route-price {
    position: absolute; left: 0; right: 0; top: 330px;
    font-family: "Oswald", sans-serif; font-weight: 700; font-size: 34px; color: var(--white);
  }
  .photo-white { background: radial-gradient(circle at 45% 55%, #f4f4f2 0%, #c9c7c0 45%, #6b6a5e 100%); }
  .photo-black { background: radial-gradient(circle at 50% 60%, #2a2a2a 0%, #111 50%, #8a6a4a 100%); }
  .photo-green { background: radial-gradient(circle at 55% 60%, #b6dc6a 0%, #9cc85a 45%, #7a8a7a 100%); }
  .photo-yellow { background: radial-gradient(circle at 50% 60%, #f3b23a 0%, #e09a22 45%, #8a8a88 100%); }

  .baseline { position: absolute; left: 14px; top: 644px; width: 1156px; height: 10px; background: var(--white); }
  .reflection {
    position: absolute; left: 14px; top: 654px; width: 1156px; height: 36px;
    background: linear-gradient(180deg, var(--mist) 0%, rgba(133,202,230,0.7) 40%, rgba(206,233,245,0.6) 100%);
  }
</style>
</head>
<body>
  <section class="banner">
    <div class="skyline" role="img" aria-label="Faint city skyline silhouette"></div>

    <div class="brand">
      <span class="brand-square"></span>
      <span class="brand-name">DORVAN'S TAXI</span>
    </div>

    <h1 class="headline">Dorvan's Taxis Are At Your Service</h1>

    <div class="promo">
      <p class="promo-offer"><span class="amount">$35</span> off to HOLMBRIDGE Airport</p>
      <p class="promo-code">USE PROMOCODE PW12</p>
    </div>

    <div class="route" style="left:425px;">
      <p class="route-label">To Holmbridge<br>Airport</p>
      <span class="route-tick"></span>
      <div class="route-photo photo-white" role="img" aria-label="White sedan taxi"></div>
      <p class="route-price">$40</p>
    </div>
    <div class="route" style="left:593px;">
      <p class="route-label">To LMV<br>Airport</p>
      <span class="route-tick"></span>
      <div class="route-photo photo-black" role="img" aria-label="Black luxury SUV at a hotel entrance"></div>
      <p class="route-price">$125</p>
    </div>
    <div class="route" style="left:765px;">
      <p class="route-label">To JRT<br>Airport</p>
      <span class="route-tick"></span>
      <div class="route-photo photo-green" role="img" aria-label="Lime green city taxi"></div>
      <p class="route-price">$140</p>
    </div>
    <div class="route" style="left:947px;">
      <p class="route-label" style="top:60px;">To PMR<br>Airport</p>
      <span class="route-tick"></span>
      <div class="route-photo photo-yellow" role="img" aria-label="Yellow taxi cab on a city street"></div>
      <p class="route-price">$190</p>
    </div>
  </section>
  <div class="baseline"></div>
  <div class="reflection"></div>
</body>
</html>
```